11 x 11 Flyer Design for Social Media - Reverse Mortgages

62 or older?

A Reverse Mortgage
could be
Your Road to Financial Freedom

* No Monthly Payments
* No Income Requirements
* No Credit Score Requirements
* No Loss of Ownership

Receive cash by lump sum, monthly installments or a line of credit!!

Call us today for a Free Consultation!!
(800) 471-2965

Bluegate Financial Services, Inc.
NMLS #318760
www.bluegatehome.com

```html
<!DOCTYPE html>
<html lang="en">
<head>
<meta charset="utf-8">
<title>Reverse Mortgage Flyer – Bluegate Financial Services, Inc.</title>
<link href="https://fonts.googleapis.com/css2?family=Open+Sans:ital,wght@0,400;0,600;0,700;1,700&display=swap" rel="stylesheet">
<style>
  :root {
    --brand-blue: #1e5da6;
    --brand-green: #8dc63f;
    --brand-green-dark: #5f8f25;
    --ink: #2f3a2a;
    --white: #ffffff;
    --photo-sand: #c9c2b4;
    --photo-sky: #9fb7c8;
    --photo-warm: #a7744f;
    --photo-red: #a8322f;
    --divider-gold: #e6d7a0;
  }
  * { margin: 0; padding: 0; box-sizing: border-box; }
  html, body { width: 1200px; height: 1200px; overflow: hidden; }
  body {
    background: var(--brand-blue);
    font-family: "Open Sans", Arial, sans-serif;
  }
  .flyer {
    position: relative;
    width: 1200px;
    height: 1200px;
    background: var(--brand-blue);
  }
  .card {
    position: absolute;
    left: 42px; top: 42px;
    width: 1116px; height: 1113px;
    background: var(--white);
    overflow: hidden;
  }
  .hero-shapes { position: absolute; left: 0; top: 0; }
  .brand {
    position: absolute;
    left: 120px; top: 60px;
    display: flex; align-items: center; gap: 14px;
  }
  .brand-dot {
    width: 46px; height: 46px; border-radius: 50%;
    background: var(--brand-blue); flex: none;
  }
  .brand-name {
    font-weight: 700; font-size: 26px; line-height: 1.2;
    color: var(--brand-blue); width: 260px;
  }
  .headline {
    position: absolute;
    left: 34px; top: 255px;
    font-style: italic; font-weight: 700;
    font-size: 51px; line-height: 66px;
    color: var(--white);
  }
  .cta-label {
    position: absolute; left: 64px; top: 458px;
    font-weight: 600; font-size: 22px; color: var(--ink);
  }
  .cta-phone {
    position: absolute; left: 86px; top: 498px;
    font-weight: 700; font-size: 50px; color: var(--white);
    letter-spacing: 0.5px;
  }
  .age-question {
    position: absolute; left: 34px; top: 633px;
    font-weight: 700; font-size: 53px; line-height: 62px;
    color: var(--brand-blue);
  }
  .benefits {
    position: absolute; left: 310px; top: 645px;
    list-style: none;
    display: grid; grid-template-columns: 378px 380px; row-gap: 38px;
  }
  .benefits li {
    display: flex; align-items: center; gap: 14px;
    font-size: 24px; color: var(--brand-blue); white-space: nowrap;
  }
  .benefits svg { flex: none; }
  .payout-banner {
    position: absolute; left: 104px; top: 785px;
    width: 910px; height: 72px;
    background: var(--brand-blue);
    clip-path: polygon(10px 0, 100% 0, calc(100% - 10px) 100%, 0 100%);
    display: flex; align-items: center; justify-content: center;
    font-weight: 700; font-size: 22px; color: var(--white);
  }
  .photo { position: absolute; }
  .photo-hero {
    left: 534px; top: 0; width: 582px; height: 599px;
    background: linear-gradient(160deg, var(--photo-sky) 0%, var(--photo-sand) 55%, #e9e6df 100%);
  }
  .photo-row { position: absolute; left: 0; top: 849px; width: 1116px; height: 203px; display: flex; gap: 7px; background: var(--divider-gold); }
  .photo-row .photo { position: static; height: 100%; }
  .photo-car { width: 360px; background: linear-gradient(135deg, #7d8e6a, #3d3b36 70%); }
  .photo-phone { width: 379px; background: linear-gradient(120deg, var(--photo-warm) 0%, var(--photo-red) 60%, #e7ddd0 100%); }
  .photo-selfie { width: 363px; background: linear-gradient(150deg, #a9c0d3, #6b5548 75%); }
  .footer {
    position: absolute; left: 0; top: 1052px; width: 1116px; height: 61px;
    display: flex; align-items: center; justify-content: space-between;
    padding: 0 30px 0 34px;
    font-size: 19px; font-weight: 600; color: var(--brand-blue);
  }
  .footer-web { display: flex; align-items: center; gap: 14px; }
</style>
</head>
<body>
<div class="flyer">
  <div class="card">
    <div class="photo photo-hero" role="img" aria-label="Smiling senior couple embracing on a beach"></div>

    <svg class="hero-shapes" width="1116" height="600" viewBox="0 0 1116 600" aria-hidden="true">
      <polygon points="0,0 632,0 584,185 0,185" fill="var(--white)"/>
      <polygon points="584,185 620,140 658,185" fill="var(--brand-green-dark)"/>
      <polygon points="0,185 658,185 534,599 0,599" fill="var(--brand-green)"/>
    </svg>

    <div class="brand">
      <span class="brand-dot"></span>
      <span class="brand-name">Bluegate Financial Services, Inc.</span>
    </div>

    <h1 class="headline">A Reverse Mortgage<br>could be Your Road<br>to Financial Freedom</h1>
    <p class="cta-label">Call us today for a Free Consultation!!</p>
    <p class="cta-phone">(800) 471-2965</p>

    <h2 class="age-question">62 OR<br>OLDER?</h2>
    <ul class="benefits">
      <li><svg width="18" height="16" viewBox="0 0 18 16"><path d="M1 8l5 6L17 1" fill="none" stroke="var(--brand-green)" stroke-width="3"/></svg>No Monthly Payments</li>
      <li><svg width="18" height="16" viewBox="0 0 18 16"><path d="M1 8l5 6L17 1" fill="none" stroke="var(--brand-green)" stroke-width="3"/></svg>No Credit Score Requirements</li>
      <li><svg width="18" height="16" viewBox="0 0 18 16"><path d="M1 8l5 6L17 1" fill="none" stroke="var(--brand-green)" stroke-width="3"/></svg>No Income Requirements</li>
      <li><svg width="18" height="16" viewBox="0 0 18 16"><path d="M1 8l5 6L17 1" fill="none" stroke="var(--brand-green)" stroke-width="3"/></svg>No Loss of Ownership</li>
    </ul>

    <div class="photo-row">
      <div class="photo photo-car" role="img" aria-label="Senior couple smiling in a convertible car"></div>
      <div class="photo photo-phone" role="img" aria-label="Woman checking her phone at home"></div>
      <div class="photo photo-selfie" role="img" aria-label="Happy senior couple taking a selfie"></div>
    </div>

    <div class="payout-banner">Receive cash by lump sum, monthly installments or a line of credit!!</div>

    <footer class="footer">
      <span class="footer-company">Bluegate Financial Services, Inc. / NMLS #318760</span>
      <span class="footer-web">
        <svg width="28" height="28" viewBox="0 0 28 28" aria-hidden="true">
          <circle cx="14" cy="14" r="13" fill="var(--brand-blue)"/>
          <path d="M7 9c3 0 4 2 6 2s1 4 -1 5-2 4-1 6M17 5c0 3 3 3 4 5s-2 3 0 6 3 1 3 1" fill="none" stroke="var(--white)" stroke-width="1.6"/>
        </svg>
        www.bluegatehome.com
      </span>
    </footer>
  </div>
</div>
</body>
</html>
```